WE HAND MAKE AND DECORATE BEAUTIFUL CREATIVE GINGER BREAD HOUSES FOR CHRISTMAS AND CUPCAKES FOR SPECIAL OCCASIONS

Contact Information for Business Card

MAPLE AND THISTLE DESIGNS
FLORA 0467 213 809
BRENDA 0455038216

```html
<!DOCTYPE html>
<html lang="en">
<head>
<meta charset="utf-8">
<title>Maple and Thistle Designs – Business Card</title>
<link rel="stylesheet" href="https://fonts.googleapis.com/css2?family=Allura&family=Sniglet:wght@800&family=Tinos&display=swap">
<style>
  :root {
    --card-red: #ab1916;
    --cream: #ffffff;
    --leaf-green: #6f9a3c;
    --ginger-tan: #c9b57a;
  }
  * { margin: 0; padding: 0; box-sizing: border-box; }
  html, body {
    width: 1200px;
    height: 741px;
    overflow: hidden;
    background: var(--card-red);
  }
  .card {
    position: relative;
    width: 1200px;
    height: 741px;
    background: var(--card-red);
    color: var(--cream);
  }
  .brand {
    position: absolute;
    left: 76px;
    top: 96px;
    display: flex;
    align-items: center;
    gap: 36px;
  }
  .brand-mark {
    width: 150px;
    height: 150px;
    background: var(--ginger-tan);
  }
  .brand-name {
    font-family: "Allura", cursive;
    font-size: 72px;
    line-height: 1.1;
    color: var(--cream);
  }
  .tagline {
    position: absolute;
    left: 0;
    top: 318px;
    width: 100%;
    text-align: center;
    font-family: "Allura", cursive;
    font-size: 56px;
    line-height: 88px;
    color: var(--cream);
  }
  .contacts {
    position: absolute;
    top: 592px;
    left: 100px;
    right: 88px;
    display: flex;
    justify-content: space-between;
  }
  .contact {
    display: flex;
    align-items: baseline;
    gap: 26px;
  }
  .contact-name {
    font-family: "Sniglet", sans-serif;
    font-weight: 800;
    font-size: 44px;
    letter-spacing: 1px;
    color: var(--leaf-green);
  }
  .contact-phone {
    font-family: "Tinos", serif;
    font-size: 41px;
    color: var(--leaf-green);
  }
</style>
</head>
<body>
  <main class="card">
    <header class="brand">
      <div class="brand-mark" aria-hidden="true"></div>
      <h1 class="brand-name">Maple and Thistle Designs</h1>
    </header>

    <p class="tagline">“Handmade and decorated christmas gingerbread<br>houses and special occasion cupcakes”</p>

    <footer class="contacts">
      <div class="contact">
        <span class="contact-name">FLORA</span>
        <span class="contact-phone">0467 213 809</span>
      </div>
      <div class="contact">
        <span class="contact-name">BRENDA</span>
        <span class="contact-phone">0455038216</span>
      </div>
    </footer>
  </main>
</body>
</html>
```